Varnel Supply requires a new business card.

We are an online professional tool store.

Target Market(s)

We target the professional technician.

Industry/Entity Type

Business

Contact Information for Business Card

VarnelSupply.com.au

sales@varnelsupply.example

Requirements
Must have
• Needs to look commercial and professional
Should not have
• No Australian Colors, maps or shapes.
• No Shapes of Tools

```html
<!DOCTYPE html>
<html lang="en">
<head>
<meta charset="utf-8">
<title>Varnel Supply – Business Card</title>
<link href="https://fonts.googleapis.com/css2?family=PT+Sans:wght@400;700&family=Exo+2:wght@700&display=swap" rel="stylesheet">
<style>
  :root {
    --backdrop: #2b2b2b;
    --paper: #f3f3f3;
    --royal: #0c22a8;
    --sky: #1592c4;
    --teal-card: #0c89b5;
    --white: #ffffff;
  }
  * { margin: 0; padding: 0; box-sizing: border-box; }
  html, body { width: 1200px; height: 960px; overflow: hidden; }
  body {
    background: var(--backdrop);
    font-family: "PT Sans", Arial, sans-serif;
    position: relative;
  }
  .card {
    position: absolute;
    width: 600px;
    height: 342px;
    border-radius: 22px;
    overflow: hidden;
  }
  .card-front { left: 314px; top: 114px; background: var(--paper); }
  .card-back { left: 311px; top: 473px; background: var(--teal-card); }

  .wave { position: absolute; inset: 0; width: 600px; height: 342px; }

  .brand {
    position: absolute;
    display: flex;
    align-items: center;
    gap: 12px;
    font-weight: 700;
    white-space: nowrap;
  }
  .brand-dot { border-radius: 50%; flex: none; }
  .card-front .brand { left: 74px; top: 74px; font-size: 32px; color: var(--royal); }
  .card-front .brand-dot { width: 26px; height: 26px; background: var(--sky); }
  .card-back .brand { left: 50%; top: 150px; transform: translateX(-50%); font-size: 42px; color: var(--white); }
  .card-back .brand-dot { width: 34px; height: 34px; background: var(--white); }

  .holder { position: absolute; right: 28px; top: 192px; text-align: right; font-family: "Exo 2", Arial, sans-serif; }
  .holder-name { font-size: 19px; color: var(--sky); letter-spacing: 0.3px; line-height: 22px; }
  .holder-role { font-size: 15px; color: var(--white); line-height: 20px; }

  .contact-list { position: absolute; right: 28px; top: 246px; list-style: none; }
  .contact-list li {
    display: flex; justify-content: flex-end; align-items: center; gap: 8px;
    font-size: 14.5px; color: var(--white); line-height: 19.5px;
  }
  .contact-list svg { width: 14px; height: 14px; fill: var(--sky); }

  .address { position: absolute; left: 28px; top: 266px; font-size: 14.5px; line-height: 19.5px; color: var(--white); }

  .web-line {
    position: absolute; left: 0; right: 0; top: 298px; text-align: center;
    font-size: 15px; letter-spacing: 2.6px; color: var(--white);
  }
</style>
</head>
<body>
  <section class="card card-front">
    <svg class="wave" viewBox="0 0 600 342" aria-hidden="true">
      <path d="M0,116 C80,200 180,236 285,226 C400,212 480,150 600,168 L600,342 L0,342 Z" fill="var(--royal)"/>
      <path d="M20,170 C120,235 250,240 340,214 C430,186 500,142 600,158 L600,166 C500,152 430,196 340,224 C240,252 110,238 20,170 Z" fill="var(--white)"/>
      <path d="M60,190 C160,236 260,234 345,210 C430,186 500,146 600,152 L600,158 C500,150 430,194 345,220 C250,246 150,240 60,190 Z" fill="var(--sky)"/>
    </svg>
    <div class="brand"><span class="brand-dot"></span>Varnel Supply</div>
    <div class="holder">
      <div class="holder-name">MAREK HOLT</div>
      <div class="holder-role">PRESIDENT</div>
    </div>
    <ul class="contact-list">
      <li>555 0142 7781 <svg viewBox="0 0 14 14"><path d="M1,5 Q7,0 13,5 L11,7 L9,5.5 L5,5.5 L3,7 Z M3,8 L11,8 L12,13 L2,13 Z"/></svg></li>
      <li>555 0193 4426 <svg viewBox="0 0 14 14"><path d="M4,0 H10 A1,1 0 0 1 11,1 V13 A1,1 0 0 1 10,14 H4 A1,1 0 0 1 3,13 V1 A1,1 0 0 1 4,0 Z M4.5,2 V11 H9.5 V2 Z"/></svg></li>
      <li>555 0167 3358 <svg viewBox="0 0 14 14"><path d="M3,1 H10 V5 H3 Z M1,6 H13 V13 H1 Z M3,8 H11 V9 H3 Z"/></svg></li>
      <li>sales@varnelsupply.example <svg viewBox="0 0 14 14"><path d="M1,3 H13 V4 L7,8 L1,4 Z M1,5.5 L7,9.5 L13,5.5 V11 H1 Z"/></svg></li>
    </ul>
    <p class="address">2190 Harwell Road<br>Lindale Park, NY 10482<br>VarnelSupply.com.au</p>
  </section>

  <section class="card card-back">
    <div class="brand"><span class="brand-dot"></span>Varnel Supply</div>
    <p class="web-line">www.VarnelSupply.com.au</p>
  </section>
</body>
</html>
```